Working Capital graphics

Our business advisory firm requires 9 images to be re-created and improved in the branding of our business.

The 9 images have been uploaded below and the colours and branding of the business can be found at the website www.thornwickadvisory.com.au

```html
<!DOCTYPE html>
<html lang="en">
<head>
<meta charset="utf-8">
<title>Working Capital Graphics</title>
<link rel="stylesheet" href="https://fonts.googleapis.com/css2?family=Montserrat:ital,wght@0,500;0,600;0,700;1,600;1,700&display=swap">
<style>
  :root{
    --bg:#efefef;
    --panel:#ffffff;
    --navy:#1b2d66;
    --deep:#0f2a5c;
    --royal:#1f56c2;
    --darkblue:#1a3d8f;
    --blue:#0aa6ea;
    --sky:#35b9f0;
    --pale:#6ccdf5;
    --orange:#f7931e;
  }
  html,body{margin:0;padding:0;width:1200px;height:541px;overflow:hidden;background:var(--bg);}
  .board{display:block;width:1200px;height:541px;font-family:"Montserrat",sans-serif;}
  .panel{fill:var(--panel);}
  .lbl{font-size:9.5px;font-weight:600;fill:var(--navy);text-anchor:middle;}
  .hub{font-size:15px;font-weight:600;fill:var(--blue);text-anchor:middle;}
  .tag-box{fill:#fff;stroke:var(--orange);stroke-width:1.6;}
  .tag{font-size:9px;font-weight:600;fill:var(--navy);text-anchor:middle;}
  .flow{stroke:var(--orange);stroke-width:1.6;fill:none;marker-end:url(#tip);}
  .tri-txt{font-size:10px;font-weight:600;fill:#fff;text-anchor:middle;}
  .seg{stroke:#fff;stroke-width:3;}
  .seg-txt{font-size:9px;font-weight:600;fill:#fff;text-anchor:middle;}
  .orbit{fill:none;stroke:var(--navy);stroke-width:1.5;}
  .bubble{fill:#fff;stroke:var(--pale);stroke-width:1.5;}
  .bubble-o{fill:none;stroke:var(--orange);stroke-width:1.5;}
  .bub-txt{font-size:6.5px;font-weight:700;fill:var(--navy);text-anchor:middle;}
  .big-orange{font-size:23px;font-weight:700;fill:var(--orange);text-anchor:middle;}
  .head{font-weight:700;fill:var(--navy);text-anchor:middle;}
  .tree{stroke:var(--blue);stroke-width:1.4;fill:none;}
  .box-o{fill:#fff;stroke:var(--orange);stroke-width:1.5;}
  .box-b{fill:#fff;stroke:var(--blue);stroke-width:1.5;}
  .num{fill:var(--orange);}
  .num-b{fill:var(--blue);}
  .num-txt{font-weight:700;fill:#fff;text-anchor:middle;}
  .small{font-size:6px;font-weight:600;fill:var(--navy);text-anchor:middle;}
  .axis{stroke:var(--blue);stroke-width:2.5;}
  .dash{stroke:var(--blue);stroke-width:1.6;stroke-dasharray:6 5;}
  .ray{stroke:var(--blue);stroke-width:2.4;marker-end:url(#tipb);}
  .tick{font-size:16px;font-weight:600;fill:var(--navy);}
  .letter{font-size:21px;font-weight:700;fill:var(--navy);}
  .note{font-size:14px;font-weight:600;fill:var(--navy);}
  .node{fill:#fff;stroke:var(--blue);stroke-width:3;}
  .node-arc{fill:none;stroke:var(--orange);stroke-width:3;}
  .node-txt{font-size:13px;font-weight:600;fill:var(--navy);text-anchor:middle;}
  .spoke{stroke:var(--navy);stroke-width:3;}
</style>
</head>
<body>
<svg class="board" viewBox="0 0 2576 1161" xmlns="http://www.w3.org/2000/svg">
  <defs>
    <marker id="tip" viewBox="0 0 10 10" refX="8" refY="5" markerWidth="5" markerHeight="5" orient="auto"><path d="M0 0L10 5L0 10z" fill="#f7931e"/></marker>
    <marker id="tipb" viewBox="0 0 10 10" refX="8" refY="5" markerWidth="5" markerHeight="5" orient="auto"><path d="M0 0L10 5L0 10z" fill="#0aa6ea"/></marker>
  </defs>

  <!-- Cycles -->
  <g class="cycles">
    <rect class="panel" x="23" y="15" width="626" height="550"/>
    <text class="lbl" x="117" y="70"><tspan x="117">CASH</tspan><tspan x="117" dy="10">MANAGEMENT</tspan></text>
    <text class="lbl" x="188" y="58"><tspan x="188">CUSTOMER</tspan><tspan x="188" dy="10">STRATEGY</tspan></text>
    <text class="lbl" x="264" y="63"><tspan x="264">SALES</tspan><tspan x="264" dy="10">MANAGEMENT</tspan></text>
    <text class="lbl" x="278" y="92"><tspan x="278">RISK</tspan><tspan x="278" dy="11">MANAGEMENT</tspan></text>
    <text class="lbl" x="302" y="131"><tspan x="302">CONTRACT</tspan><tspan x="302" dy="10">MANAGEMENT</tspan></text>
    <text class="lbl" x="293" y="173"><tspan x="293">SALES ORDER</tspan><tspan x="293" dy="10">PROCESSING</tspan></text>
    <text class="lbl" x="255" y="211"><tspan x="255">CREDIT</tspan><tspan x="255" dy="10">CHECK</tspan></text>
    <text class="lbl" x="195" y="226"><tspan x="195">ORDER</tspan><tspan x="195" dy="10">FULFILLMENT</tspan></text>
    <text class="lbl" x="128" y="226">BILLING</text>
    <text class="lbl" x="97" y="193"><tspan x="97">CUSTOMER</tspan><tspan x="97" dy="10">SERVICE</tspan></text>
    <text class="lbl" x="84" y="150"><tspan x="84">CASH</tspan><tspan x="84" dy="10">COLLECTION</tspan></text>
    <text class="lbl" x="92" y="106"><tspan x="92">RECEIPT &amp;</tspan><tspan x="92" dy="10">ALLOCATION</tspan><tspan x="92" dy="10">OF CASH</tspan></text>
    <text class="hub" x="189" y="142"><tspan x="189">REVENUE</tspan><tspan x="189" dy="17">MANAGEMENT</tspan></text>
    <rect class="tag-box" x="136" y="245" width="101" height="17"/>
    <text class="tag" x="186" y="257">CUSTOMER TO CASH</text>

    <text class="lbl" x="486" y="55"><tspan x="486">PURCHASING</tspan><tspan x="486" dy="10">STRATEGY</tspan></text>
    <text class="lbl" x="560" y="68"><tspan x="560">RISK</tspan><tspan x="560" dy="11">MANAGEMENT</tspan></text>
    <text class="lbl" x="586" y="102"><tspan x="586">CONTRACT</tspan><tspan x="586" dy="10">MANAGEMENT</tspan></text>
    <text class="lbl" x="592" y="145"><tspan x="592">SALES ORDER</tspan><tspan x="592" dy="10">PROCESSING</tspan></text>
    <text class="lbl" x="563" y="189"><tspan x="563">CREDIT</tspan><tspan x="563" dy="11">CHECK</tspan></text>
    <text class="lbl" x="489" y="213"><tspan x="489">SALES ORDER</tspan><tspan x="489" dy="11">PROCESSING</tspan></text>
    <text class="lbl" x="418" y="186"><tspan x="418">RISK</tspan><tspan x="418" dy="11">MANAGEMENT</tspan></text>
    <text class="lbl" x="383" y="140"><tspan x="383">CASH</tspan><tspan x="383" dy="11">COLLECTION</tspan></text>
    <text class="lbl" x="388" y="116">WAREHOUSING</text>
    <text class="lbl" x="417" y="81">DRISTIBUTION</text>
    <text class="hub" x="487" y="135"><tspan x="487">SUPPLY CHAIN</tspan><tspan x="487" dy="16">MANAGEMENT</tspan></text>
    <rect class="tag-box" x="428" y="240" width="123" height="18"/>
    <text class="tag" x="489" y="252">FORECAST TO FULFILLMENT</text>

    <path d="M338 210L420 291H256Z" fill="var(--blue)"/>
    <text class="tri-txt" transform="translate(312 250) rotate(-45)">A/R</text>
    <text class="tri-txt" transform="translate(362 246) rotate(45)">INVENTORY</text>
    <text class="tri-txt" x="338" y="280">A/P</text>

    <text class="lbl" x="341" y="332"><tspan x="341">PURCHASING</tspan><tspan x="341" dy="11">STRATEGY</tspan></text>
    <text class="lbl" x="269" y="350"><tspan x="269">CASH</tspan><tspan x="269" dy="11">MANAGEMENT</tspan></text>
    <text class="lbl" x="414" y="355"><tspan x="414">CASH</tspan><tspan x="414" dy="11">MANAGEMENT</tspan></text>
    <text class="lbl" x="446" y="391"><tspan x="446">CUSTOMER</tspan><tspan x="446" dy="11">SERVICE</tspan></text>
    <text class="lbl" x="441" y="435"><tspan x="441">CUSTOMER</tspan><tspan x="441" dy="11">SERVICE</tspan></text>
    <text class="lbl" x="421" y="467"><tspan x="421">CASH</tspan><tspan x="421" dy="11">COLLECTION</tspan></text>
    <text class="lbl" x="339" y="488"><tspan x="339">CASH</tspan><tspan x="339" dy="11">COLLECTION</tspan></text>
    <text class="lbl" x="261" y="468"><tspan x="261">RISK</tspan><tspan x="261" dy="11">MANAGEMENT</tspan></text>
    <text class="lbl" x="238" y="434"><tspan x="238">CUSTOMER</tspan><tspan x="238" dy="11">SERVICE</tspan></text>
    <text class="lbl" x="235" y="389"><tspan x="235">CASH</tspan><tspan x="235" dy="11">COLLECTION</tspan></text>
    <text class="hub" x="342" y="407"><tspan x="342">EXPENDITURE</tspan><tspan x="342" dy="16">MANAGEMENT</tspan></text>
    <rect class="tag-box" x="287" y="514" width="101" height="18"/>
    <text class="tag" x="337" y="526">PURCHASE TO PAY</text>

    <g>
      <line class="flow" x1="150" y1="70" x2="163" y2="63"/>
      <line class="flow" x1="212" y1="63" x2="228" y2="68"/>
      <line class="flow" x1="240" y1="78" x2="250" y2="86"/>
      <line class="flow" x1="268" y1="114" x2="272" y2="126"/>
      <line class="flow" x1="275" y1="146" x2="276" y2="160"/>
      <line class="flow" x1="262" y1="190" x2="258" y2="201"/>
      <line class="flow" x1="236" y1="215" x2="224" y2="221"/>
      <line class="flow" x1="165" y1="225" x2="152" y2="222"/>
      <line class="flow" x1="110" y1="214" x2="102" y2="205"/>
      <line class="flow" x1="108" y1="178" x2="107" y2="166"/>
      <line class="flow" x1="103" y1="143" x2="103" y2="131"/>
      <line class="flow" x1="120" y1="98" x2="128" y2="88"/>
      <line class="flow" x1="510" y1="58" x2="523" y2="64"/>
      <line class="flow" x1="550" y1="86" x2="556" y2="97"/>
      <line class="flow" x1="570" y1="118" x2="571" y2="132"/>
      <line class="flow" x1="570" y1="160" x2="567" y2="173"/>
      <line class="flow" x1="542" y1="203" x2="530" y2="210"/>
      <line class="flow" x1="455" y1="213" x2="443" y2="207"/>
      <line class="flow" x1="407" y1="176" x2="404" y2="163"/>
      <line class="flow" x1="404" y1="133" x2="405" y2="121"/>
      <line class="flow" x1="414" y1="100" x2="419" y2="89"/>
      <line class="flow" x1="448" y1="66" x2="460" y2="60"/>
      <line class="flow" x1="294" y1="242" x2="283" y2="230"/>
      <line class="flow" x1="380" y1="241" x2="392" y2="229"/>
      <line class="flow" x1="341" y1="300" x2="341" y2="316"/>
      <line class="flow" x1="372" y1="336" x2="385" y2="344"/>
      <line class="flow" x1="410" y1="372" x2="414" y2="384"/>
      <line class="flow" x1="420" y1="409" x2="420" y2="422"/>
      <line class="flow" x1="416" y1="451" x2="412" y2="460"/>
      <line class="flow" x1="385" y1="480" x2="372" y2="487"/>
      <line class="flow" x1="307" y1="487" x2="296" y2="481"/>
      <line class="flow" x1="268" y1="457" x2="268" y2="446"/>
      <line class="flow" x1="258" y1="420" x2="258" y2="407"/>
      <line class="flow" x1="265" y1="379" x2="268" y2="369"/>
      <line class="flow" x1="293" y1="342" x2="306" y2="336"/>
    </g>
  </g>

  <!-- Sales volume wheel -->
  <g class="wheel">
    <rect class="panel" x="659" y="15" width="626" height="550"/>
    <circle class="orbit" cx="975" cy="290" r="170"/>
    <path class="seg" fill="var(--sky)" d="M921 141.5A158 158 0 0 1 1029 141.5L1011.9 188.5A108 108 0 0 0 938.1 188.5Z"/>
    <path class="seg" fill="#1e9be0" d="M1034.2 143.5A158 158 0 0 1 1123.5 236L1076.5 253.1A108 108 0 0 0 1015.5 189.9Z"/>
    <path class="seg" fill="var(--orange)" d="M1123.5 236A158 158 0 0 1 1076.6 411L1044.4 372.7A108 108 0 0 0 1076.5 253.1Z"/>
    <path class="seg" fill="var(--deep)" d="M1076.6 411A158 158 0 0 1 908.2 433.1L929.3 387.8A108 108 0 0 0 1044.4 372.7Z"/>
    <path class="seg" fill="var(--darkblue)" d="M908.2 433.1A158 158 0 0 1 826.5 344L873.5 327A108 108 0 0 0 929.3 387.8Z"/>
    <path class="seg" fill="var(--royal)" d="M826.5 344A158 158 0 0 1 869.3 172.6L902.7 209.8A108 108 0 0 0 873.5 327Z"/>
    <path class="seg" fill="var(--pale)" d="M869.3 172.6A158 158 0 0 1 915.8 143.5L934.5 189.9A108 108 0 0 0 902.7 209.8Z"/>
    <text class="seg-txt" x="960" y="166">0$</text>
    <text class="seg-txt" transform="translate(1048 190) rotate(42)">COST OF SALES</text>
    <text class="seg-txt" transform="translate(1103 278) rotate(-82)"><tspan x="0">OPERATING</tspan><tspan x="0" dy="10">EXPENSES</tspan></text>
    <text class="seg-txt" transform="translate(1093 333) rotate(-68)"><tspan x="0">COSTS</tspan><tspan x="0" dy="10">FIXED</tspan></text>
    <text class="seg-txt" transform="translate(1028 405) rotate(-25)">DIVIDENDS  INTEREST  TAX</text>
    <text class="seg-txt" transform="translate(866 373) rotate(60)">DAYS</text>
    <text class="seg-txt" transform="translate(898 408) rotate(40)">DAYS</text>
    <text class="seg-txt" transform="translate(940 428) rotate(15)">DAYS</text>
    <text class="seg-txt" transform="translate(846 275) rotate(-85)"><tspan x="0">ADDITIONAL</tspan><tspan x="0" dy="10">DEBT</tspan></text>
    <text class="seg-txt" transform="translate(906 190) rotate(-45)"><tspan x="0">CASH</tspan><tspan x="0" dy="9">SHORTFALL</tspan></text>
    <text class="big-orange" x="973" y="284">NEXT $100 OF</text>
    <text class="big-orange" x="973" y="311">SALES VOLUME</text>

    <g>
      <line x1="968" y1="100" x2="968" y2="121" stroke="var(--pale)" stroke-width="1.5"/>
      <line x1="1145" y1="210" x2="1128" y2="218" stroke="var(--pale)" stroke-width="1.5"/>
      <line x1="1136" y1="390" x2="1120" y2="375" stroke="var(--pale)" stroke-width="1.5"/>
      <line x1="978" y1="482" x2="978" y2="460" stroke="var(--pale)" stroke-width="1.5"/>
      <line x1="800" y1="372" x2="820" y2="362" stroke="var(--pale)" stroke-width="1.5"/>
      <line x1="806" y1="200" x2="822" y2="212" stroke="var(--pale)" stroke-width="1.5"/>
      <circle cx="968" cy="121" r="3" fill="var(--blue)"/><circle cx="1128" cy="218" r="3" fill="var(--blue)"/>
      <circle cx="1120" cy="375" r="3" fill="var(--blue)"/><circle cx="978" cy="460" r="3" fill="var(--blue)"/>
      <circle cx="820" cy="362" r="3" fill="var(--blue)"/><circle cx="822" cy="212" r="3" fill="var(--blue)"/>
      <circle class="bubble" cx="968" cy="72" r="28"/><path class="bubble-o" d="M940 72A28 28 0 0 1 968 44"/>
      <circle class="bubble" cx="1172" cy="197" r="28"/><path class="bubble-o" d="M1172 169A28 28 0 0 1 1200 197"/>
      <circle class="bubble" cx="1163" cy="400" r="28"/><path class="bubble-o" d="M1191 400A28 28 0 0 1 1163 428"/>
      <circle class="bubble" cx="978" cy="510" r="28"/><path class="bubble-o" d="M978 538A28 28 0 0 1 950 510"/>
      <circle class="bubble" cx="773" cy="381" r="28"/><path class="bubble-o" d="M745 381A28 28 0 0 0 773 409"/>
      <circle class="bubble" cx="779" cy="188" r="28"/><path class="bubble-o" d="M751 188A28 28 0 0 1 779 160"/>
      <text class="bub-txt" x="968" y="70"><tspan x="968">REVENUE</tspan><tspan x="968" dy="8">0$</tspan></text>
      <text class="bub-txt" x="1172" y="192"><tspan x="1172">GROSS</tspan><tspan x="1172" dy="8">MARGINS</tspan><tspan x="1172" dy="8">0$</tspan></text>
      <text class="bub-txt" x="1163" y="398"><tspan x="1163">EBIT</tspan><tspan x="1163" dy="8">0$</tspan></text>
      <text class="bub-txt" x="978" y="506"><tspan x="978">RETAINED</tspan><tspan x="978" dy="8">INCOME</tspan><tspan x="978" dy="8">0$</tspan></text>
      <text class="bub-txt" x="773" y="372"><tspan x="773">AFTER</tspan><tspan x="773" dy="7">WORKING</tspan><tspan x="773" dy="7">CAPITAL</tspan><tspan x="773" dy="7">0$</tspan></text>
      <text class="bub-txt" x="779" y="179"><tspan x="779">AFTER</tspan><tspan x="779" dy="7">ADDITIONAL</tspan><tspan x="779" dy="7">FUNDING</tspan><tspan x="779" dy="7">0$</tspan></text>
    </g>
  </g>

  <!-- Receivables tree -->
  <g class="receivables">
    <rect class="panel" x="1293" y="15" width="625" height="550"/>
    <text class="head" x="1380" y="137" font-size="12">RECEIVABLES</text>
    <text class="head" x="1486" y="134" font-size="8">SUB-PROCESS</text>
    <text class="head" x="1634" y="134" font-size="8">DRIVERS</text>
    <text class="head" x="1803" y="134" font-size="8">SUB-DRIVERS</text>
    <path class="tree" d="M1423 277H1434M1434 177V393M1434 177H1443M1434 278H1443M1434 393H1443
      M1538 177H1546M1546 152V202M1546 152H1553M1546 177H1553M1546 202H1553
      M1538 278H1546M1546 253V303M1546 253H1553M1546 278H1553M1546 303H1553
      M1538 393H1546M1546 368V418M1546 368H1553M1546 393H1553M1546 418H1553
      M1702 200H1718M1718 190V259M1718 190H1733M1718 210H1733M1718 240H1733M1718 259H1733
      M1702 278H1718M1718 284V346M1718 284H1733M1718 303H1733M1718 322H1733M1718 346H1733
      M1702 393H1718M1718 366V447M1718 366H1733M1718 385H1733M1718 409H1733M1718 428H1733M1718 447H1733"/>
    <rect class="box-o" x="1337" y="254" width="86" height="45"/>
    <text class="head" x="1380" y="273" font-size="8.5"><tspan x="1380">RECEIVABLES</tspan><tspan x="1380" dy="11">DRIVERS</tspan></text>
    <g>
      <rect class="box-o" x="1443" y="168" width="95" height="18"/><text class="small" x="1491" y="180">LOREM IPSUM</text>
      <rect class="box-o" x="1443" y="269" width="95" height="18"/><text class="small" x="1491" y="281">LOREM IPSUM</text>
      <rect class="box-o" x="1443" y="384" width="95" height="18"/><text class="small" x="1491" y="396">LOREM IPSUM</text>
    </g>
    <g>
      <rect class="box-b" x="1553" y="144" width="149" height="17"/><circle class="num" cx="1563" cy="152" r="10"/><text class="num-txt" x="1563" y="156" font-size="10">14</text><text class="small" x="1634" y="155">LOREM IPSUM DOLOR SIT</text>
      <rect class="box-b" x="1553" y="169" width="149" height="17"/><circle class="num" cx="1563" cy="177" r="10"/><text class="num-txt" x="1563" y="181" font-size="10">15</text><text class="small" x="1634" y="180">LOREM IPSUM DOLOR SIT</text>
      <rect class="box-b" x="1553" y="194" width="149" height="17"/><circle class="num" cx="1563" cy="202" r="10"/><text class="num-txt" x="1563" y="206" font-size="10">16</text><text class="small" x="1634" y="205">LOREM IPSUM DOLOR SIT</text>
      <rect class="box-b" x="1553" y="245" width="149" height="17"/><circle class="num" cx="1563" cy="253" r="10"/><text class="num-txt" x="1563" y="257" font-size="10">14</text><text class="small" x="1634" y="256">LOREM IPSUM DOLOR SIT</text>
      <rect class="box-b" x="1553" y="270" width="149" height="17"/><circle class="num" cx="1563" cy="278" r="10"/><text class="num-txt" x="1563" y="282" font-size="10">15</text><text class="small" x="1634" y="281">LOREM IPSUM DOLOR SIT</text>
      <rect class="box-b" x="1553" y="295" width="149" height="17"/><circle class="num" cx="1563" cy="303" r="10"/><text class="num-txt" x="1563" y="307" font-size="10">16</text><text class="small" x="1634" y="306">LOREM IPSUM DOLOR SIT</text>
      <rect class="box-b" x="1553" y="360" width="149" height="17"/><circle class="num" cx="1563" cy="368" r="10"/><text class="num-txt" x="1563" y="372" font-size="10">14</text><text class="small" x="1634" y="371">LOREM IPSUM DOLOR SIT</text>
      <rect class="box-b" x="1553" y="385" width="149" height="17"/><circle class="num" cx="1563" cy="393" r="10"/><text class="num-txt" x="1563" y="397" font-size="10">15</text><text class="small" x="1634" y="396">LOREM IPSUM DOLOR SIT</text>
      <rect class="box-b" x="1553" y="410" width="149" height="17"/><circle class="num" cx="1563" cy="418" r="10"/><text class="num-txt" x="1563" y="422" font-size="10">16</text><text class="small" x="1634" y="421">LOREM IPSUM DOLOR SIT</text>
    </g>
    <g>
      <rect class="box-o" x="1733" y="183" width="140" height="14"/><text class="small" x="1803" y="192">LOREM IPSUM</text>
      <rect class="box-o" x="1733" y="203" width="140" height="14"/><text class="small" x="1803" y="212">LOREM IPSUM</text>
      <rect class="box-o" x="1733" y="233" width="140" height="14"/><text class="small" x="1803" y="242">LOREM IPSUM</text>
      <rect class="box-o" x="1733" y="252" width="140" height="14"/><text class="small" x="1803" y="261">LOREM IPSUM</text>
      <rect class="box-o" x="1733" y="277" width="140" height="14"/><text class="small" x="1803" y="286">LOREM IPSUM</text>
      <rect class="box-o" x="1733" y="296" width="140" height="14"/><text class="small" x="1803" y="305">LOREM IPSUM</text>
      <rect class="box-o" x="1733" y="315" width="140" height="14"/><text class="small" x="1803" y="324">LOREM IPSUM</text>
      <rect class="box-o" x="1733" y="339" width="140" height="14"/><text class="small" x="1803" y="348">LOREM IPSUM</text>
      <rect class="box-o" x="1733" y="359" width="140" height="14"/><text class="small" x="1803" y="368">LOREM IPSUM</text>
      <rect class="box-o" x="1733" y="378" width="140" height="14"/><text class="small" x="1803" y="387">LOREM IPSUM</text>
      <rect class="box-o" x="1733" y="402" width="140" height="14"/><text class="small" x="1803" y="411">LOREM IPSUM</text>
      <rect class="box-o" x="1733" y="421" width="140" height="14"/><text class="small" x="1803" y="430">LOREM IPSUM</text>
      <rect class="box-o" x="1733" y="440" width="140" height="14"/><text class="small" x="1803" y="449">LOREM IPSUM</text>
    </g>
  </g>

  <!-- Absorption chart -->
  <g class="absorption">
    <rect class="panel" x="1928" y="15" width="626" height="550"/>
    <text x="2016" y="70" font-size="13.5" font-style="italic" font-weight="700" fill="var(--navy)">NET WORKING CAPITAL ABSORPTION</text>
    <g text-anchor="end">
      <text class="tick" x="2065" y="113">450m</text><text class="tick" x="2065" y="163">450m</text>
      <text class="tick" x="2065" y="213">450m</text><text class="tick" x="2065" y="263">450m</text>
      <text class="tick" x="2065" y="313">450m</text><text class="tick" x="2065" y="363">450m</text>
      <text class="tick" x="2065" y="413">450m</text><text class="tick" x="2065" y="463">450m</text>
    </g>
    <g text-anchor="middle">
      <text class="tick" x="2111" y="498">20m</text><text class="tick" x="2171" y="498">20m</text>
      <text class="tick" x="2230" y="498">20m</text><text class="tick" x="2290" y="498">20m</text>
      <text class="tick" x="2350" y="498">20m</text><text class="tick" x="2410" y="498">20m</text>
      <text class="note" x="2265" y="526">NET WORKING CAPITAL (NWC)</text>
    </g>
    <line class="axis" x1="2078" y1="95" x2="2078" y2="474"/>
    <line class="axis" x1="2077" y1="473" x2="2447" y2="473"/>
    <path fill="var(--orange)" d="M2261 282V164A118 118 0 0 0 2148 282A118 118 0 0 0 2266 400V282Z"/>
    <path fill="var(--orange)" d="M2266 282V400A117 117 0 0 0 2383 282Z"/>
    <g stroke="#fff" stroke-width="2.5">
      <line x1="2266" y1="282" x2="2150" y2="282"/><line x1="2266" y1="282" x2="2266" y2="400"/>
    </g>
    <line class="dash" x1="2078" y1="282" x2="2395" y2="282"/>
    <line class="dash" x1="2266" y1="282" x2="2266" y2="473"/>
    <line class="ray" x1="2266" y1="282" x2="2266" y2="132"/>
    <line class="ray" x1="2266" y1="282" x2="2344" y2="166"/>
    <line class="ray" x1="2266" y1="282" x2="2404" y2="282"/>
    <line class="ray" x1="2266" y1="282" x2="2349" y2="380"/>
    <line class="ray" x1="2266" y1="282" x2="2156" y2="370"/>
    <line class="ray" x1="2266" y1="282" x2="2166" y2="165"/>
    <circle cx="2266" cy="282" r="9" fill="var(--blue)" stroke="#fff" stroke-width="2"/>
    <text class="letter" x="2264" y="120">B</text>
    <text class="letter" x="2342" y="155">C</text><text class="note" x="2368" y="148">LOREM IPSUM</text>
    <text class="letter" x="2401" y="273">D</text><text class="note" x="2432" y="259"><tspan x="2432">LOREM</tspan><tspan x="2432" dy="17">IPSUM</tspan></text>
    <text class="letter" x="2362" y="388">E</text><text class="note" x="2391" y="388">LOREM IPSUM</text>
    <text class="letter" x="2136" y="390">F</text><text class="note" x="2131" y="417">LOREM IPSUM</text>
    <text class="letter" x="2156" y="176">A</text><text class="note" x="2110" y="148">LOREM IPSUM</text>
  </g>

  <!-- Working capitals hub -->
  <g class="hub-chart">
    <rect class="panel" x="321" y="574" width="636" height="559"/>
    <g>
      <line class="spoke" x1="635" y1="717" x2="635" y2="747"/>
      <line class="spoke" x1="720" y1="748" x2="706" y2="770"/>
      <line class="spoke" x1="771" y1="826" x2="743" y2="835"/>
      <line class="spoke" x1="752" y1="929" x2="729" y2="914"/>
      <line class="spoke" x1="686" y1="986" x2="674" y2="961"/>
      <line class="spoke" x1="584" y1="986" x2="597" y2="961"/>
      <line class="spoke" x1="518" y1="929" x2="541" y2="914"/>
      <line class="spoke" x1="497" y1="828" x2="526" y2="836"/>
      <line class="spoke" x1="550" y1="748" x2="564" y2="771"/>
    </g>
    <circle cx="635" cy="857" r="110" fill="none" stroke="var(--navy)" stroke-width="4"/>
    <g fill="var(--navy)">
      <circle cx="635" cy="747" r="4.5"/><circle cx="706" cy="773" r="4.5"/><circle cx="743" cy="837" r="4.5"/>
      <circle cx="729" cy="912" r="4.5"/><circle cx="673" cy="960" r="4.5"/><circle cx="597" cy="960" r="4.5"/>
      <circle cx="541" cy="912" r="4.5"/><circle cx="527" cy="837" r="4.5"/><circle cx="564" cy="773" r="4.5"/>
    </g>
    <circle cx="635" cy="857" r="93" fill="var(--blue)"/>
    <text x="635" y="852" font-size="29" font-weight="700" fill="#fff" text-anchor="middle">WORKING</text>
    <text x="635" y="886" font-size="29" font-weight="700" fill="#fff" text-anchor="middle">CAPITALS</text>
    <g>
      <circle class="node" cx="634" cy="670" r="47"/><circle class="node-arc" cx="634" cy="670" r="47" pathLength="100" stroke-dasharray="45 55" transform="rotate(-70 634 670)"/>
      <circle class="node" cx="754" cy="713" r="47"/><circle class="node-arc" cx="754" cy="713" r="47" pathLength="100" stroke-dasharray="40 60" transform="rotate(20 754 713)"/>
      <circle class="node" cx="818" cy="823" r="47"/><circle class="node-arc" cx="818" cy="823" r="47" pathLength="100" stroke-dasharray="40 60" transform="rotate(170 818 823)"/>
      <circle class="node" cx="797" cy="950" r="47"/><circle class="node-arc" cx="797" cy="950" r="47" pathLength="100" stroke-dasharray="45 55" transform="rotate(100 797 950)"/>
      <circle class="node" cx="699" cy="1032" r="47"/><circle class="node-arc" cx="699" cy="1032" r="47" pathLength="100" stroke-dasharray="45 55" transform="rotate(-20 699 1032)"/>
      <circle class="node" cx="571" cy="1032" r="47"/><circle class="node-arc" cx="571" cy="1032" r="47" pathLength="100" stroke-dasharray="45 55" transform="rotate(-100 571 1032)"/>
      <circle class="node" cx="473" cy="950" r="47"/><circle class="node-arc" cx="473" cy="950" r="47" pathLength="100" stroke-dasharray="45 55" transform="rotate(-10 473 950)"/>
      <circle class="node" cx="450" cy="824" r="47"/><circle class="node-arc" cx="450" cy="824" r="47" pathLength="100" stroke-dasharray="40 60" transform="rotate(110 450 824)"/>
      <circle class="node" cx="514" cy="713" r="47"/><circle class="node-arc" cx="514" cy="713" r="47" pathLength="100" stroke-dasharray="45 55" transform="rotate(-20 514 713)"/>
      <text class="node-txt" x="634" y="666"><tspan x="634">LOREM</tspan><tspan x="634" dy="16">IPSUM</tspan></text>
      <text class="node-txt" x="754" y="709"><tspan x="754">LOREM</tspan><tspan x="754" dy="16">IPSUM</tspan></text>
      <text class="node-txt" x="818" y="819"><tspan x="818">LOREM</tspan><tspan x="818" dy="16">IPSUM</tspan></text>
      <text class="node-txt" x="797" y="946"><tspan x="797">LOREM</tspan><tspan x="797" dy="16">IPSUM</tspan></text>
      <text class="node-txt" x="699" y="1028"><tspan x="699">LOREM</tspan><tspan x="699" dy="16">IPSUM</tspan></text>
      <text class="node-txt" x="571" y="1028"><tspan x="571">LOREM</tspan><tspan x="571" dy="16">IPSUM</tspan></text>
      <text class="node-txt" x="473" y="946"><tspan x="473">LOREM</tspan><tspan x="473" dy="16">IPSUM</tspan></text>
      <text class="node-txt" x="450" y="820"><tspan x="450">LOREM</tspan><tspan x="450" dy="16">IPSUM</tspan></text>
      <text class="node-txt" x="514" y="709"><tspan x="514">LOREM</tspan><tspan x="514" dy="16">IPSUM</tspan></text>
    </g>
  </g>

  <!-- Payables tree -->
  <g class="payables">
    <rect class="panel" x="969" y="574" width="635" height="559"/>
    <text class="head" x="1088" y="714" font-size="17">PAYABLES</text>
    <text class="head" x="1393" y="714" font-size="17">DRIVERS</text>
    <rect class="box-o" x="1018" y="835" width="141" height="73"/>
    <text class="head" x="1088" y="867" font-size="16"><tspan x="1088">PAYABLES</tspan><tspan x="1088" dy="20">DRIVERS</tspan></text>
    <path class="tree" d="M1159 871H1194M1194 752V988M1194 752H1210M1194 814H1210M1194 871H1210M1194 929H1210M1194 988H1210"/>
    <g>
      <rect class="box-o" x="1225" y="736" width="330" height="33"/><line x1="1225" y1="769" x2="1548" y2="769" stroke="var(--blue)" stroke-width="1.5"/>
      <rect class="box-o" x="1225" y="798" width="330" height="33"/><line x1="1225" y1="831" x2="1548" y2="831" stroke="var(--blue)" stroke-width="1.5"/>
      <rect class="box-o" x="1225" y="855" width="330" height="33"/><line x1="1225" y1="888" x2="1548" y2="888" stroke="var(--blue)" stroke-width="1.5"/>
      <rect class="box-o" x="1225" y="913" width="330" height="33"/><line x1="1225" y1="946" x2="1548" y2="946" stroke="var(--blue)" stroke-width="1.5"/>
      <rect class="box-o" x="1225" y="972" width="330" height="33"/><line x1="1225" y1="1005" x2="1548" y2="1005" stroke="var(--blue)" stroke-width="1.5"/>
      <circle class="num-b" cx="1225" cy="752" r="18"/><text class="num-txt" x="1225" y="759" font-size="19">14</text>
      <circle class="num-b" cx="1225" cy="814" r="18"/><text class="num-txt" x="1225" y="821" font-size="19">15</text>
      <circle class="num-b" cx="1225" cy="871" r="18"/><text class="num-txt" x="1225" y="878" font-size="19">16</text>
      <circle class="num-b" cx="1225" cy="929" r="18"/><text class="num-txt" x="1225" y="936" font-size="19">17</text>
      <circle class="num-b" cx="1225" cy="988" r="18"/><text class="num-txt" x="1225" y="995" font-size="19">18</text>
      <text class="head" x="1393" y="757" font-size="13">LOREM IPSUM DOLOR SIT</text>
      <text class="head" x="1393" y="819" font-size="13">LOREM IPSUM DOLOR SIT</text>
      <text class="head" x="1393" y="876" font-size="13">LOREM IPSUM DOLOR SIT</text>
      <text class="head" x="1393" y="934" font-size="13">LOREM IPSUM DOLOR SIT</text>
      <text class="head" x="1393" y="993" font-size="13">LOREM IPSUM DOLOR SIT</text>
    </g>
  </g>

  <!-- Inventories tree -->
  <g class="inventories">
    <rect class="panel" x="1613" y="574" width="635" height="559"/>
    <text class="head" x="1710" y="662" font-size="16">INVENTORIES</text>
    <text class="head" x="1909" y="662" font-size="13">DRIVER GROUP</text>
    <text class="head" x="2105" y="662" font-size="13">SUB-GROUP</text>
    <rect class="box-b" x="1650" y="827" width="121" height="63"/>
    <text class="head" x="1710" y="854" font-size="13"><tspan x="1710">INVENTORY</tspan><tspan x="1710" dy="16">DRIVERS</tspan></text>
    <path class="tree" d="M1771 858H1813M1813 737V1023M1813 737H1830M1813 842H1830M1813 931H1830M1813 1023H1830
      M1969 737H1988M1988 691V781M1988 691H2007M1988 721H2007M1988 751H2007M1988 781H2007
      M1969 842H1988M1988 811V872M1988 811H2007M1988 842H2007M1988 872H2007
      M1969 931H1988M1988 902V957M1988 902H2007M1988 930H2007M1988 957H2007
      M1969 1023H1988M1988 993V1053M1988 993H2007M1988 1023H2007M1988 1053H2007"/>
    <g>
      <rect class="box-o" x="1845" y="725" width="124" height="24"/><circle class="num-b" cx="1845" cy="737" r="15"/><text class="num-txt" x="1845" y="743" font-size="15">10</text>
      <rect class="box-o" x="1845" y="830" width="124" height="24"/><circle class="num-b" cx="1845" cy="842" r="15"/><text class="num-txt" x="1845" y="848" font-size="15">11</text>
      <rect class="box-o" x="1845" y="919" width="124" height="24"/><circle class="num-b" cx="1845" cy="931" r="15"/><text class="num-txt" x="1845" y="937" font-size="15">12</text>
      <rect class="box-o" x="1845" y="1011" width="124" height="24"/><circle class="num-b" cx="1845" cy="1023" r="15"/><text class="num-txt" x="1845" y="1029" font-size="15">13</text>
      <g font-size="10" font-style="italic" font-weight="700" fill="var(--navy)" text-anchor="middle">
        <text x="1909" y="741">LOREM IPSUM</text><text x="1909" y="846">LOREM IPSUM</text>
        <text x="1909" y="935">LOREM IPSUM</text><text x="1909" y="1027">LOREM IPSUM</text>
      </g>
    </g>
    <g>
      <rect class="box-b" x="2007" y="682" width="197" height="17"/><text class="small" x="2105" y="694" font-size="8">LOREM IPSUM</text>
      <rect class="box-b" x="2007" y="712" width="197" height="17"/><text class="small" x="2105" y="724" font-size="8">LOREM IPSUM</text>
      <rect class="box-b" x="2007" y="742" width="197" height="17"/><text class="small" x="2105" y="754" font-size="8">LOREM IPSUM</text>
      <rect class="box-b" x="2007" y="772" width="197" height="17"/><text class="small" x="2105" y="784" font-size="8">LOREM IPSUM</text>
      <rect class="box-b" x="2007" y="802" width="197" height="17"/><text class="small" x="2105" y="814" font-size="8">LOREM IPSUM</text>
      <rect class="box-b" x="2007" y="833" width="197" height="17"/><text class="small" x="2105" y="845" font-size="8">LOREM IPSUM</text>
      <rect class="box-b" x="2007" y="863" width="197" height="17"/><text class="small" x="2105" y="875" font-size="8">LOREM IPSUM</text>
      <rect class="box-b" x="2007" y="893" width="197" height="17"/><text class="small" x="2105" y="905" font-size="8">LOREM IPSUM</text>
      <rect class="box-b" x="2007" y="921" width="197" height="17"/><text class="small" x="2105" y="933" font-size="8">LOREM IPSUM</text>
      <rect class="box-b" x="2007" y="948" width="197" height="17"/><text class="small" x="2105" y="960" font-size="8">LOREM IPSUM</text>
      <rect class="box-b" x="2007" y="984" width="197" height="17"/><text class="small" x="2105" y="996" font-size="8">LOREM IPSUM</text>
      <rect class="box-b" x="2007" y="1014" width="197" height="17"/><text class="small" x="2105" y="1026" font-size="8">LOREM IPSUM</text>
      <rect class="box-b" x="2007" y="1044" width="197" height="17"/><text class="small" x="2105" y="1056" font-size="8">LOREM IPSUM</text>
    </g>
  </g>
</svg>
</body>
</html>
```